Web Design

Qorvane Institute offers a one stop solution for people to be introduced to the world of Forex trading. We have interactive forex room, one on one coaching by our experienced trading experts.
Main menus:
1. Learn to trade
2. About us
3. Brokers
4. Money management and risk
5. FAQ
6. Register – scroll down menu with registration form (name, email and register button)
7. Contact us
The webpage should have:
1. Large text style and images
2. Join / Get Started Buttons
3. Instructors profile
4. People Testimonies
5. Recommended Brokers
6. Live rates
7. Live support
8. Social icons: facebook, twitter and g+

```html
<!DOCTYPE html>
<html lang="en">
<head>
<meta charset="utf-8">
<title>Qorvane Institute – Learn Forex Trading Online</title>
<link rel="stylesheet" href="https://fonts.googleapis.com/css2?family=Lato:wght@400;700;900&family=Open+Sans:wght@400;600;700&display=swap">
<style>
  :root {
    --navy: #0f2a44;
    --blue: #1b9ad8;
    --green: #77b300;
    --green-btn: #6fb017;
    --white: #ffffff;
    --text-grey: #3b4651;
    --line: #d6dbe0;
    --up: #9fe11f;
    --down: #ff2a2a;
  }
  * { margin: 0; padding: 0; box-sizing: border-box; }
  html, body { width: 1200px; height: 2408px; overflow: hidden; background: var(--white); }
  body { position: relative; font-family: "Open Sans", Arial, sans-serif; color: var(--navy); }

  /* Header */
  .site-header { position: absolute; left: 0; top: 0; width: 1200px; height: 100px; background: var(--white); }
  .brand { position: absolute; left: 50px; top: 28px; display: flex; align-items: center; gap: 12px; }
  .brand-mark { width: 22px; height: 22px; background: var(--green); }
  .brand-name { font-family: "Lato", sans-serif; font-weight: 900; font-size: 30px; color: var(--navy); letter-spacing: 0.5px; }
  .main-nav { position: absolute; right: 48px; top: 38px; display: flex; align-items: center; font-family: "Lato", sans-serif; font-weight: 700; font-size: 14.5px; color: var(--navy); }
  .main-nav span.sep { width: 6px; height: 6px; border-radius: 50%; background: var(--green); margin: 0 11px; }

  /* Hero */
  .hero { position: absolute; left: 0; top: 100px; width: 1200px; height: 590px; overflow: hidden; }
  .hero-photo { position: absolute; inset: 0; background: linear-gradient(100deg, #e9eef2 0%, #d7dfe6 30%, #c9d3dc 55%, #b9c5cf 75%, #dfe6ec 100%); }
  .hero-title { position: absolute; left: 126px; top: 80px; font-family: "Lato", sans-serif; font-weight: 900; font-size: 46px; line-height: 50px; color: var(--navy); }
  .hero-sub { position: absolute; left: 126px; top: 196px; font-family: "Lato", sans-serif; font-weight: 700; font-size: 24px; line-height: 29px; color: var(--blue); }
  .btn-start { position: absolute; left: 126px; top: 296px; width: 194px; height: 56px; border-radius: 5px; background: var(--green-btn); color: var(--white); font-family: "Lato", sans-serif; font-weight: 700; font-size: 24px; display: flex; align-items: center; justify-content: center; }

  /* Section titles */
  .section-title { position: absolute; left: 0; width: 1200px; text-align: center; font-family: "Lato", sans-serif; font-weight: 900; font-size: 30px; color: var(--navy); }
  .section-sub { position: absolute; left: 0; width: 1200px; text-align: center; font-size: 17px; color: var(--navy); letter-spacing: 0.5px; }

  /* Instructors */
  .instructor { position: absolute; top: 838px; width: 300px; text-align: center; }
  .instructor-photo { width: 236px; height: 236px; margin: 0 auto; border-radius: 50%; background: radial-gradient(circle at 50% 40%, #d9b9a2 0%, #b89a88 35%, #8a9aa8 70%, #c8d2da 100%); }
  .instructor-name { margin-top: 38px; font-family: "Lato", sans-serif; font-weight: 900; font-size: 16px; letter-spacing: 1px; color: var(--navy); }
  .instructor-role { font-size: 15px; letter-spacing: 1px; color: var(--text-grey); }

  /* Testimonial */
  .testimonial { position: absolute; left: 0; top: 1196px; width: 1200px; height: 284px; }
  .testimonial-photo { position: absolute; inset: 0; background: linear-gradient(90deg, #0e2a45 0%, #1c3a56 40%, #3b5570 75%, #56697c 100%); }
  .testimonial-avatar { position: absolute; left: 80px; top: 56px; width: 132px; height: 132px; border-radius: 50%; background: radial-gradient(circle at 50% 40%, #f1d9c4 0%, #d9b99d 45%, #b7a58e 100%); }
  .testimonial-quote { position: absolute; left: 252px; top: 70px; width: 930px; font-size: 18.5px; line-height: 30px; color: var(--white); letter-spacing: 0.6px; }
  .testimonial-author { position: absolute; left: 254px; top: 166px; font-size: 12px; color: #c9d2da; letter-spacing: 1px; }
  .testimonial-author b { color: var(--green); font-weight: 600; }
  .slider-dots { position: absolute; left: 562px; top: 242px; display: flex; gap: 18px; }
  .slider-dots i { width: 10px; height: 10px; border-radius: 50%; background: #4b6b3b; }
  .slider-dots i.active { background: var(--green); }

  /* Brokers */
  .broker-row { position: absolute; left: 52px; top: 1650px; width: 1096px; height: 64px; display: flex; align-items: center; }
  .broker { flex: 1; text-align: center; font-family: "Lato", sans-serif; font-weight: 700; font-size: 26px; color: var(--navy); }
  .broker-divider { width: 1px; height: 62px; background: var(--line); }

  /* Rates */
  .rates { position: absolute; left: 0; top: 1786px; width: 1200px; height: 200px; background: linear-gradient(180deg, #0c2238 0%, #123250 55%, #1e4a70 100%); }
  .rate { position: absolute; top: 70px; width: 150px; text-align: center; }
  .rate-pair { font-family: "Lato", sans-serif; font-weight: 700; font-size: 20px; color: var(--white); }
  .rate-value { margin-top: 4px; font-size: 17px; color: var(--white); }
  .up { color: var(--up); }
  .down { color: var(--down); }

  /* Stay connected */
  .connect { position: absolute; left: 0; top: 1986px; width: 1200px; height: 422px; background: var(--green); color: var(--white); }
  .connect-title { position: absolute; left: 0; width: 1200px; top: 28px; text-align: center; font-family: "Lato", sans-serif; font-weight: 900; font-size: 30px; }
  .connect-sub { position: absolute; left: 0; width: 1200px; top: 64px; text-align: center; font-size: 17px; }
  .contact-item { position: absolute; top: 118px; width: 180px; text-align: center; }
  .contact-icon { width: 70px; height: 70px; margin: 0 auto; display: block; }
  .contact-label { margin-top: 24px; font-family: "Lato", sans-serif; font-weight: 700; font-size: 18px; white-space: nowrap; }
  .footer-line { position: absolute; left: 50px; top: 324px; width: 1100px; height: 1px; background: rgba(255,255,255,0.35); }
  .copyright { position: absolute; left: 0; width: 1200px; top: 356px; text-align: center; font-size: 13px; }
</style>
</head>
<body>

<header class="site-header">
  <div class="brand"><span class="brand-mark"></span><span class="brand-name">Qorvane</span></div>
  <nav class="main-nav">
    <span>LEARN TO TRADE</span><span class="sep"></span>
    <span>ABOUT US</span><span class="sep"></span>
    <span>BROKERS</span><span class="sep"></span>
    <span>MONEY MANAGEMENT AND RISK</span><span class="sep"></span>
    <span>FAQ</span><span class="sep"></span>
    <span>REGISTER</span><span class="sep"></span>
    <span>CONTACT US</span>
  </nav>
</header>

<section class="hero">
  <div class="hero-photo" role="img" aria-label="Photo of a smiling trader in a striped shirt with colleagues talking in a bright office"></div>
  <h1 class="hero-title">LEARN FOREX<br>TRADING ONLINE</h1>
  <p class="hero-sub">FIND COURSES SUITED<br>TO TRADERS AT ALL LEVELS</p>
  <div class="btn-start">GET STARTED</div>
</section>

<h2 class="section-title" style="top:736px;">OUR INSTRUCTORS</h2>
<p class="section-sub" style="top:770px;">We Educate People</p>

<div class="instructor" style="left:54px;">
  <div class="instructor-photo" role="img" aria-label="Portrait photo of the chief instructor"></div>
  <div class="instructor-name">MARLO KESTRIN</div>
  <div class="instructor-role">Chief Instructor</div>
</div>
<div class="instructor" style="left:448px; top:836px;">
  <div class="instructor-photo" role="img" aria-label="Portrait photo of the expert analyst"></div>
  <div class="instructor-name">TEODOR VASS</div>
  <div class="instructor-role">Expert Analyst</div>
</div>
<div class="instructor" style="left:840px;">
  <div class="instructor-photo" role="img" aria-label="Portrait photo of an instructor on the phone"></div>
  <div class="instructor-name">DANE HOLLOWAY</div>
  <div class="instructor-role">Instructor</div>
</div>

<section class="testimonial">
  <div class="testimonial-photo" role="img" aria-label="Dark blue toned photo of an applauding audience"></div>
  <div class="testimonial-avatar" role="img" aria-label="Portrait photo of the client giving the testimonial"></div>
  <p class="testimonial-quote">"It is amazing how powerful and easy-to-use Qorvane Instructions.<br>And some of them are actually fantastic. Stop wasting your money on hiring someone else, invest in your business wisely!"</p>
  <p class="testimonial-author"><b>Lissa Wrenfield</b> | Meridane Capital</p>
  <div class="slider-dots"><i class="active"></i><i></i><i></i></div>
</section>

<h2 class="section-title" style="top:1544px;">RECOMMENDED BROKERS</h2>
<p class="section-sub" style="top:1580px;">Choose one of the recommended brokers.</p>
<div class="broker-row">
  <div class="broker">Avelund Markets</div>
  <div class="broker-divider"></div>
  <div class="broker">Brontal FX</div>
  <div class="broker-divider"></div>
  <div class="broker">Helvion Bank</div>
  <div class="broker-divider"></div>
  <div class="broker">Ostrava Exchange</div>
</div>

<section class="rates" role="img" aria-label="Live currency rates over a dark blue market chart background">
  <div class="rate" style="left:71px;"><div class="rate-pair">EUR/USD</div><div class="rate-value"><span class="up">1.2489</span> | <span class="up">+0.11%</span></div></div>
  <div class="rate" style="left:221px;"><div class="rate-pair">EUR/USD</div><div class="rate-value"><span class="down">1.5743</span> | <span class="down">-0.3%</span></div></div>
  <div class="rate" style="left:373px;"><div class="rate-pair">USD/JPY</div><div class="rate-value"><span class="down">117.74</span> | <span class="down">-0.1%</span></div></div>
  <div class="rate" style="left:521px;"><div class="rate-pair">USD/CHF</div><div class="rate-value"><span class="up">0.9630</span> | <span class="up">+0.5%</span></div></div>
  <div class="rate" style="left:671px;"><div class="rate-pair">AUD/USD</div><div class="rate-value"><span class="up">0.8553</span> | <span class="up">+0.18%</span></div></div>
  <div class="rate" style="left:819px;"><div class="rate-pair">USD/CAD</div><div class="rate-value"><span class="down">1.1328</span> | <span class="down">-0.3%</span></div></div>
  <div class="rate" style="left:967px;"><div class="rate-pair">BTC/USD</div><div class="rate-value"><span class="up">117.74</span> | <span class="up">+0.1%</span></div></div>
</section>

<footer class="connect">
  <h2 class="connect-title">STAY CONNECTED</h2>
  <p class="connect-sub">Claritas est etiam processus dynamicus</p>

  <div class="contact-item" style="left:46px;">
    <svg class="contact-icon" viewBox="0 0 70 70" fill="none" stroke="#fff" stroke-width="3">
      <circle cx="35" cy="35" r="32"/>
      <path d="M24 20 L30 19 L33 27 L29 30 Q32 38 40 41 L43 37 L51 40 L50 46 Q46 51 38 48 Q24 42 20 28 Q20 22 24 20 Z" fill="#fff" stroke="none"/>
    </svg>
    <div class="contact-label">+1 555 010 2468</div>
  </div>

  <div class="contact-item" style="left:231px;">
    <svg class="contact-icon" viewBox="0 0 70 70" fill="none" stroke="#fff" stroke-width="3">
      <circle cx="35" cy="35" r="32"/>
      <path d="M35 20 C45 20 52 26 52 34 C52 42 45 48 35 48 C32 48 30 47.5 28 47 L20 51 L22 44 C19 41 18 38 18 34 C18 26 25 20 35 20 Z" stroke-width="2.6"/>
      <line x1="27" y1="31" x2="43" y2="31" stroke-width="2.4"/>
      <line x1="27" y1="37" x2="43" y2="37" stroke-width="2.4"/>
    </svg>
    <div class="contact-label">Live Chat</div>
  </div>

  <div class="contact-item" style="left:420px;">
    <svg class="contact-icon" viewBox="0 0 70 70" fill="none" stroke="#fff" stroke-width="3">
      <circle cx="35" cy="35" r="32"/>
      <rect x="20" y="25" width="30" height="21" stroke-width="2.6"/>
      <path d="M20 25 L35 37 L50 25" stroke-width="2.6"/>
    </svg>
    <div class="contact-label">help@qorvane.example</div>
  </div>

  <div class="contact-item" style="left:604px;">
    <svg class="contact-icon" viewBox="0 0 70 70" fill="none" stroke="#fff" stroke-width="3"><circle cx="35" cy="35" r="32"/></svg>
    <div class="contact-label">qorvane.institute</div>
  </div>

  <div class="contact-item" style="left:789px;">
    <svg class="contact-icon" viewBox="0 0 70 70" fill="none" stroke="#fff" stroke-width="3"><circle cx="35" cy="35" r="32"/></svg>
    <div class="contact-label">@QorvaneInst</div>
  </div>

  <div class="contact-item" style="left:974px;">
    <svg class="contact-icon" viewBox="0 0 70 70" fill="none" stroke="#fff" stroke-width="3"><circle cx="35" cy="35" r="32"/></svg>
    <div class="contact-label">qorvane institute</div>
  </div>

  <div class="footer-line"></div>
  <p class="copyright">2014 <b>Qorvane Institute</b>. All rights reserved</p>
</footer>

</body>
</html>
```